Professional Sales Business looking for inspirational poster

I need an inspirational poster design for sales professionals, targeted around the phrase "Win Fast, Lose Fast". The style of the poster will be primarily minimalistic and flat with the main focus being on the phrase, however, any graphics or creative font and background styles are encouraged. Color choice is up to you.

Design Specs:
Vector files are best. If creating a vector file isn't possible, 150dpi raster images (at actual size or bigger) are good too. The poster must be in a portrait layout and scalable to the sizes of 18" X 24" and 24" X 36". Please convert all text to outlines.

Please msg me if you have any additional questions.

```html
<!DOCTYPE html>
<html lang="en">
<head>
<meta charset="utf-8">
<title>Win Fast, Lose Fast — Sales Poster</title>
<link rel="stylesheet" href="https://fonts.googleapis.com/css2?family=Playfair+Display:wght@700&display=swap">
<style>
  :root {
    --page-bg: #ececec;
    --teal: #579e98;
    --teal-deep: #4a8d87;
    --blush: #f0e8ec;
    --frame-line: #ffffff;
    --shade: rgba(0, 0, 0, 0.07);
    --glow: rgba(255, 255, 255, 0.06);
  }
  html, body {
    margin: 0;
    padding: 0;
    width: 1200px;
    height: 848px;
    overflow: hidden;
    background: var(--page-bg);
  }
  .canvas {
    position: relative;
    width: 1200px;
    height: 848px;
  }
  .poster {
    position: absolute;
    left: 346px;
    top: 88px;
    width: 507px;
    height: 673px;
    display: block;
  }
  .poster-bg { fill: var(--teal); }
  .frame-outer { fill: none; stroke: var(--frame-line); stroke-width: 2; }
  .frame-field { fill: var(--blush); }
  .upper-band { fill: var(--teal-deep); }
  .disc-top { fill: var(--blush); }
  .disc-bottom { fill: var(--teal); }
  .facet-shade { fill: var(--shade); }
  .facet-glow { fill: var(--glow); }
  .headline {
    font-family: "Playfair Display", "Didot", serif;
    font-weight: 700;
    font-size: 52px;
  }
  .headline--left { text-anchor: end; }
  .headline--right { text-anchor: start; }
  .headline--win { fill: var(--teal-deep); }
  .headline--lose { fill: var(--blush); }
  .divider-top { stroke: var(--teal-deep); stroke-width: 2; }
  .divider-bottom { stroke: var(--blush); stroke-width: 2; }
  .rack-top { fill: var(--teal-deep); }
  .rack-bottom { fill: var(--blush); }
</style>
</head>
<body>
<main class="canvas">
  <svg class="poster" viewBox="0 0 494 656" xmlns="http://www.w3.org/2000/svg" role="img" aria-label="Poster: Win fast, lose fast">
    <rect class="poster-bg" x="0" y="0" width="494" height="656"/>

    <rect class="frame-outer" x="37" y="101" width="422" height="442"/>
    <rect class="frame-field" x="43" y="107" width="410" height="430"/>
    <rect class="upper-band" x="60" y="123" width="377" height="198"/>

    <path class="disc-top" d="M88 321 A160 160 0 0 1 408 321 Z"/>
    <path class="disc-bottom" d="M88 321 A160 160 0 0 0 408 321 Z"/>

    <polygon class="facet-shade" points="0,0 247,328 0,656"/>
    <polygon class="facet-shade" points="494,0 247,328 494,656"/>
    <polygon class="facet-glow" points="0,0 494,0 247,328"/>

    <rect class="rack-top" x="234" y="176" width="22" height="18" role="img" aria-label="Small triangle of dots"/>

    <line class="divider-top" x1="245" y1="228" x2="245" y2="321"/>
    <line class="divider-bottom" x1="245" y1="321" x2="245" y2="414"/>

    <text class="headline headline--left headline--win" x="238" y="281">WIN</text>
    <text class="headline headline--right headline--win" x="253" y="281">FAST,</text>
    <text class="headline headline--left headline--lose" x="238" y="396">LOSE</text>
    <text class="headline headline--right headline--lose" x="253" y="396">FAST</text>

    <rect class="rack-bottom" x="238" y="430" width="22" height="18" role="img" aria-label="Small inverted triangle of dots"/>
    <circle class="rack-bottom" cx="234" cy="463" r="2.5"/>
  </svg>
</main>
</body>
</html>
```